Creating a label for germicidal disposable wipes.

I need to create a label to put on our containers of germicidal disposable wipes. I am attaching an example of another germicidal wipe that I would like a similar format but more customized to look like my companies.

```html
<!DOCTYPE html>
<html lang="en">
<head>
<meta charset="utf-8">
<title>Vitalis Germicidal Wipes Label</title>
<link href="https://fonts.googleapis.com/css2?family=Roboto:ital,wght@0,400;0,500;0,700;1,400;1,700&family=Roboto+Condensed:wght@700&display=swap" rel="stylesheet">
<style>
  :root {
    --backdrop: #e4e4e4;
    --label-white: #ffffff;
    --ink: #333333;
    --green: #22c24a;
    --teal: #157a6a;
    --navy: #0a0a80;
    --panel-text: #ffffff;
  }
  * { margin: 0; padding: 0; box-sizing: border-box; }
  html, body {
    width: 1200px; height: 1200px; overflow: hidden;
    background: var(--backdrop);
  }
  .canvas { position: relative; width: 1200px; height: 1200px; }
  .label {
    position: absolute; left: 140px; top: 252px;
    width: 920px; height: 696px;
    background: var(--label-white);
    border-radius: 38px; overflow: hidden;
    font-family: "Roboto", sans-serif; color: var(--ink);
  }
  .brand {
    position: absolute; right: 350px; top: 38px;
    display: flex; align-items: center; gap: 12px;
  }
  .brand-dot {
    width: 52px; height: 52px; border-radius: 50%;
    background: var(--teal);
  }
  .brand-name {
    font-family: "Roboto", sans-serif; font-weight: 500;
    font-size: 58px; line-height: 1; color: var(--ink);
  }
  .product-title {
    position: absolute; left: 31px; top: 136px;
    font-weight: 700; font-size: 73px; line-height: 79px;
    letter-spacing: -0.5px;
  }
  .claims {
    position: absolute; left: 31px; top: 622px; top: 372px;
    font-style: italic; font-weight: 700; font-size: 24.5px;
  }
  .divider {
    position: absolute; left: 0; top: 417px; width: 570px; height: 11px;
    background: linear-gradient(90deg, var(--navy), var(--teal) 50%, var(--green));
  }
  .ingredients {
    position: absolute; left: 31px; top: 443px;
    font-size: 17px; line-height: 20.5px; font-style: italic;
  }
  .ingredients h2 { font-size: 17px; font-weight: 700; }
  .ingredients p { font-weight: 400; }
  .caution {
    position: absolute; left: 31px; top: 534px;
    display: flex; align-items: center; gap: 12px;
    font-family: "Roboto Condensed", sans-serif; font-weight: 700;
  }
  .caution-word { font-size: 47px; line-height: 1; letter-spacing: 0.5px; }
  .caution-lines { display: flex; flex-direction: column; }
  .caution-main { font-size: 20px; line-height: 21px; }
  .caution-sub { font-size: 14.5px; line-height: 16px; }
  .count {
    position: absolute; left: 31px; top: 620px;
    font-weight: 500; font-size: 20px;
  }
  .count strong { font-size: 32px; font-weight: 500; }
  .info-panel {
    position: absolute; left: 600px; top: 0; width: 320px; height: 100%;
    background: linear-gradient(180deg, var(--green) 0%, var(--teal) 40%, #0c3a7a 70%, var(--navy) 100%);
    color: var(--panel-text);
    padding: 160px 28px 0 30px;
    font-size: 17.4px; line-height: 22.6px;
  }
  .info-panel h3 { font-size: 17.4px; font-weight: 700; }
  .info-panel p + p { margin-top: 22.6px; }
</style>
</head>
<body>
<div class="canvas">
  <section class="label">
    <div class="brand">
      <span class="brand-dot"></span>
      <span class="brand-name">KVR</span>
    </div>
    <h1 class="product-title">Vitalis<br>GERMICIDAL<br>WIPES</h1>
    <div class="claims">Virucidal*, Bactericidal, Tuberculocidal, Fungicidal</div>
    <div class="divider"></div>
    <div class="ingredients">
      <h2>ACTIVE INGREDIENTS:</h2>
      <p>Isopropyl Alcohol</p>
      <p>Alkyl C12-18 Dimethyl benxyl Ammonium chloride</p>
      <p>Alkyl C12-18 Dimethyl Ethyl benzyl Ammonium chloride</p>
    </div>
    <div class="caution">
      <span class="caution-word">CAUTION</span>
      <span class="caution-lines">
        <span class="caution-main">KEEP OUT OF REACH OF CHILDREN</span>
        <span class="caution-sub">DO NOT USE AS A BABY WIPE</span>
      </span>
    </div>
    <div class="count"><strong>160</strong> Wipes (6 x 6.75 in)</div>
    <aside class="info-panel">
      <h3>Lorem ipsum:</h3>
      <p>Lorem ipsum dolor sit amet, consectetuer adipiscing elit, sed diam nonummy nibh euismod tincidunt ut laoreet dolore magna aliquam erat volutpat.</p>
      <p>Ut wisi enim ad minim veniam, quis nostrud exerci tation ullam&shy;corper suscipit lobortis nisl ut aliquip ex ea commodo conse&shy;quat.</p>
      <p>Duis autem vel eum iriure dolor in hendrerit in vulputate velit esse molestie consequat, vel illum dolore eu feugiat nulla facilisis at vero eros et accumsan et iusto odio dignis&shy;sim qui blandit praesent luptatum zzril delenit augue duis dolore te feugait nulla facilisi.</p>
    </aside>
  </section>
</div>
</body>
</html>
```